Steelcrest Process Systems. Needs a Business Card Design

We need a business card design for an engineering company which supplies industrial components (pumps, compressors, mechanical seals) provides repairs and services for above mentioned equipments. We offer a uniqe engineering solutions which help our customers to increase the productivness of their manufacturings, and energy savings.

Target Market(s)

Chemical and energy plants, refineries. Food industry and private consumers in a less.

Industry/Entity Type

Business

Contact Information for Business Card

Stylish and sleek design oriented on industrial area.

Requirements
Should not have
• company name shortening

```html
<!DOCTYPE html>
<html lang="en">
<head>
<meta charset="utf-8">
<title>Steelcrest Process Systems — Business Card</title>
<link rel="stylesheet" href="https://fonts.googleapis.com/css2?family=Open+Sans:wght@400;600;700&family=Roboto+Condensed:wght@700&display=swap">
<style>
  :root {
    --brand-blue: #1c3f94;
    --brand-red: #ee3a3a;
    --card-white: #ffffff;
    --backdrop: #e9e7e3;
    --card-shadow: rgba(0, 0, 0, 0.18);
  }
  * { box-sizing: border-box; margin: 0; padding: 0; }
  html, body {
    width: 1200px;
    height: 900px;
    overflow: hidden;
    background: var(--backdrop);
    font-family: "Open Sans", Arial, sans-serif;
  }
  .canvas {
    position: relative;
    width: 1200px;
    height: 900px;
    display: flex;
    flex-direction: column;
    align-items: center;
    justify-content: center;
    gap: 40px;
  }
  .card {
    position: relative;
    width: 700px;
    height: 400px;
    background: var(--card-white);
    box-shadow: 0 6px 18px var(--card-shadow);
    overflow: hidden;
  }

  /* Front: company identity */
  .card--front {
    display: flex;
    flex-direction: column;
    align-items: center;
    justify-content: center;
    gap: 14px;
  }
  .brand-line {
    display: flex;
    align-items: center;
    gap: 14px;
  }
  .brand-dot {
    width: 26px;
    height: 26px;
    border-radius: 50%;
    background: var(--brand-red);
  }
  .brand-name {
    font-weight: 700;
    font-size: 38px;
    color: var(--brand-blue);
    letter-spacing: 0.3px;
  }
  .tagline {
    font-family: "Roboto Condensed", "Arial Narrow", sans-serif;
    font-weight: 700;
    font-size: 19px;
    color: var(--brand-blue);
  }

  /* Back: contact details */
  .corner-mark {
    position: absolute;
    left: 0;
    top: 26px;
  }
  .person {
    position: absolute;
    left: 70px;
    top: 24px;
  }
  .person-name {
    font-weight: 700;
    font-size: 22px;
    color: var(--brand-blue);
    line-height: 1.1;
  }
  .person-title {
    font-size: 16px;
    color: var(--brand-red);
  }
  .address {
    position: absolute;
    left: 60px;
    top: 120px;
    font-size: 17px;
    line-height: 1.3;
    color: var(--brand-red);
  }
  .contact-list {
    position: absolute;
    left: 40px;
    top: 180px;
    list-style: none;
    font-size: 17px;
    line-height: 1.3;
    color: var(--brand-red);
  }
  .contact-list li {
    display: flex;
    align-items: center;
    gap: 10px;
  }
  .contact-icon {
    width: 12px;
    height: 12px;
    flex: none;
  }
  .back-brand {
    position: absolute;
    right: 40px;
    top: 150px;
    display: flex;
    align-items: center;
    gap: 12px;
  }
  .back-brand .brand-name { font-size: 24px; }
  .back-brand .brand-dot { width: 20px; height: 20px; }
  .bottom-bands {
    position: absolute;
    left: 0;
    bottom: 0;
  }
</style>
</head>
<body>
<main class="canvas">

  <section class="card card--front" aria-label="Business card front">
    <div class="brand-line">
      <span class="brand-dot"></span>
      <span class="brand-name">Steelcrest Process Systems</span>
    </div>
    <p class="tagline">Repairs and services for pumps | compressors | mechanical seals</p>
  </section>

  <section class="card card--back" aria-label="Business card back">
    <svg class="corner-mark" width="58" height="40" viewBox="0 0 58 40" aria-hidden="true">
      <polygon points="0,0 30,0 0,22" fill="var(--brand-red)"/>
      <polygon points="58,0 58,40 8,40" fill="var(--brand-blue)"/>
    </svg>
    <div class="person">
      <p class="person-name">Daniel Harrow</p>
      <p class="person-title">Managing Director</p>
    </div>

    <p class="address">12345, Address Goes Here<br>Country Name, 123456.</p>

    <ul class="contact-list">
      <li>
        <svg class="contact-icon" viewBox="0 0 12 12" aria-hidden="true"><rect x="3" y="0.5" width="6" height="11" rx="1.2" fill="none" stroke="var(--brand-blue)" stroke-width="1.3"/><circle cx="6" cy="9.5" r="0.8" fill="var(--brand-blue)"/></svg>
        0145 782 310
      </li>
      <li>
        <svg class="contact-icon" viewBox="0 0 12 12" aria-hidden="true"><path d="M2.5 1 L4.5 1 L5.3 3.6 L4 4.6 Q5 7 7.4 8 L8.4 6.7 L11 7.5 L11 9.5 Q10 11.2 8 11 Q2 9.5 1 4 Q0.8 2 2.5 1 Z" fill="var(--brand-blue)"/></svg>
        044-318 902 645
      </li>
      <li>
        <svg class="contact-icon" viewBox="0 0 12 12" aria-hidden="true"><rect x="0.5" y="2" width="11" height="8" fill="var(--brand-blue)"/><path d="M0.5 2 L6 6.5 L11.5 2" fill="none" stroke="#fff" stroke-width="1"/></svg>
        info@steelcrestps.com
      </li>
      <li>
        <svg class="contact-icon" viewBox="0 0 12 12" aria-hidden="true"><circle cx="6" cy="6" r="5.5" fill="var(--brand-blue)"/><path d="M0.5 6 H11.5 M6 0.5 Q3 6 6 11.5 M6 0.5 Q9 6 6 11.5" fill="none" stroke="#fff" stroke-width="0.8"/></svg>
        www.steelcrestps.com
      </li>
    </ul>

    <div class="back-brand">
      <span class="brand-dot"></span>
      <span class="brand-name">Steelcrest Process Systems</span>
    </div>

    <svg class="bottom-bands" width="700" height="80" viewBox="0 0 700 80" aria-hidden="true">
      <polygon points="0,6 300,6 290,32 0,32" fill="var(--brand-red)"/>
      <polygon points="304,38 700,38 700,80 284,80" fill="var(--brand-blue)"/>
    </svg>
  </section>

</main>
</body>
</html>
```